Business Card for a mobile physiotherapy company

I need a layout for a business card for a mobile physiotherapy company.
Slogan is "Mobile Physiotherapy - Your Road To Recovery"
Phone number is 867-402-5913
Email VantrePhysio@mailbright.ca (subject to change with website)
Website www.VantrePhysio.ca
My name and credentials: Kent Vantre Kent Vantre, BSc(kin), MPT, CAFCI, IMS
Information maybe included: Direct Billing, Services including Physiotherapy, IMS, acupuncture
Maybe include facebook and instagram logos
One side with the logo clean and sharp
Other side with details, try not to look too busy, keep everything concise

```html
<!DOCTYPE html>
<html lang="en">
<head>
<meta charset="utf-8">
<title>Vantre Therapy – Business Card</title>
<link rel="stylesheet" href="https://fonts.googleapis.com/css2?family=Oswald:wght@600&family=Lato:ital,wght@0,400;0,700;1,400&display=swap">
<style>
  :root {
    --bg: #e9e4dc;
    --navy: #2f4a7a;
    --slate: #4d6590;
    --green: #155c4a;
    --white: #ffffff;
    --shadow: rgba(40, 30, 20, 0.22);
  }
  * { margin: 0; padding: 0; box-sizing: border-box; }
  html, body { width: 1200px; height: 1200px; overflow: hidden; background: var(--bg); }
  .stage {
    width: 1200px; height: 1200px;
    display: flex; flex-direction: column; align-items: center; justify-content: center; gap: 56px;
  }
  .card {
    position: relative; width: 900px; height: 514px; overflow: hidden;
    box-shadow: 0 10px 28px var(--shadow);
  }

  /* Brand name placeholder */
  .brand-name {
    position: absolute; left: 0; right: 0; text-align: center;
    font-family: 'Lato', sans-serif; font-weight: 700; line-height: 1;
  }

  /* Back side */
  .card-back { background: var(--slate); }
  .card-back .brand-name { top: 210px; font-size: 72px; color: var(--white); }
  .social-handle {
    position: absolute; left: 0; right: 0; bottom: 44px; text-align: center;
    font-family: 'Lato', sans-serif; font-size: 22px; color: var(--white);
  }

  /* Front side */
  .card-front { background: var(--white); }
  .card-front .brand-name { top: 150px; font-size: 62px; color: var(--green); }

  .band-person {
    position: absolute; left: 0; top: 292px; width: 470px; height: 122px;
    background: var(--navy); color: var(--white); text-align: right; padding: 22px 24px 0 0;
  }
  .person-name { font-family: 'Oswald', sans-serif; font-weight: 600; font-size: 44px; line-height: 1; text-transform: uppercase; }
  .person-creds { font-family: 'Lato', sans-serif; font-size: 21px; margin-top: 10px; }

  .band-contact {
    position: absolute; left: 482px; top: 300px; right: 0; height: 116px;
    background: var(--green); color: var(--white);
    padding: 12px 0 0 48px;
    font-family: 'Lato', sans-serif; font-size: 22px; line-height: 1.45;
  }
  .notch {
    position: absolute; left: 470px; top: 346px; width: 0; height: 0;
    border-top: 12px solid transparent; border-bottom: 12px solid transparent; border-right: 13px solid var(--green);
  }
  .contact-line { display: flex; align-items: center; gap: 10px; }
  .contact-line svg { width: 16px; height: 16px; flex: none; fill: var(--white); }

  .slogan {
    position: absolute; left: 0; top: 436px; width: 760px; text-align: center;
    font-family: 'Lato', sans-serif; font-style: italic; font-size: 22px; color: var(--green);
  }
</style>
</head>
<body>
<main class="stage">
  <section class="card card-back" aria-label="Card back">
    <p class="brand-name">Vantre Therapy</p>
    <p class="social-handle">@vantretherapy</p>
  </section>

  <section class="card card-front" aria-label="Card front">
    <p class="brand-name">Vantre Therapy</p>

    <div class="band-person">
      <p class="person-name">Kent Vantre</p>
      <p class="person-creds">BSc(kin), MPT, CAFCI, IMS</p>
    </div>

    <div class="notch"></div>
    <div class="band-contact">
      <p class="contact-line">
        <svg viewBox="0 0 16 16" aria-hidden="true"><path d="M3.6 1.2l2.3 2.6-1.3 1.9c.9 2 2.4 3.6 4.5 4.6l1.9-1.3 2.6 2.3-1.3 2.6C6.8 13.4 2.5 9.2 1.1 3.4z"/></svg>
        867-402-5913
      </p>
      <p class="contact-line">
        <svg viewBox="0 0 16 16" aria-hidden="true"><path d="M1 3h14v10H1z M2.5 4.5L8 9l5.5-4.5" fill="none" stroke="#fff" stroke-width="1.4"/></svg>
        VantrePhysio@mailbright.ca
      </p>
      <p class="contact-line">
        <svg viewBox="0 0 16 16" aria-hidden="true"><g fill="none" stroke="#fff" stroke-width="1.2"><circle cx="8" cy="8" r="6.5"/><ellipse cx="8" cy="8" rx="2.8" ry="6.5"/><path d="M1.5 8h13M2.5 5h11M2.5 11h11"/></g></svg>
        www.VantrePhysio.ca
      </p>
    </div>

    <p class="slogan">Mobile Physiotherapy - Your Road To Recovery</p>
  </section>
</main>
</body>
</html>
```